Ardenwell Building and Property Services needs a business card design

We need a business card design for our building and property services business. We already have a logo we just need a creative design and layout on a business card. Emphasis on clean, modern, professional.
Our client targets are mainly body corporates, building managers, construction managers.
We are a building services company that lean more to structural repair of buildings, through concrete rectification and carbon fibre strengthening.
We also refurbish facades, rendering, painting etc
We target higher end body corporates in prestigious locations, hence why we'd like our cards to reflect professionalism, strength, efficiency

Target Market(s)

body corporates, building managers, construction managers

Industry/Entity Type

Construction

Contact Information for Business Card

Ardenwell is the main word, with 'Building and Property Services' underneath.
Level 17, 82 Harlow Street
MERRIDALE
Melbourne
Vic 3094
T: 9518 2736
Duncan Ferris - Director
dunardenwell@mailbox-example.com

Requirements
Must have
• Stand out on the back of the card- strong/ bold, company logo
• All of the contact details written above
Should not have
• I'd like the card to stand out, especially on the back. Id like the company logo to be prominent, although feel free to be creative around it. But remain clean and professional

```html
<!DOCTYPE html>
<html lang="en">
<head>
<meta charset="utf-8">
<title>Ardenwell Building and Property Services – Business Card</title>
<link href="https://fonts.googleapis.com/css2?family=Cinzel:wght@500&family=Source+Sans+3:wght@400&display=swap" rel="stylesheet">
<style>
  :root {
    --page: #ffffff;
    --charcoal: #26282a;
    --black: #030405;
    --cyan: #0ba8df;
    --brand: #7cc6ee;
    --white: #ffffff;
    --ink: #0b0b0b;
  }
  * { margin: 0; padding: 0; box-sizing: border-box; }
  html, body {
    width: 1035px;
    height: 1200px;
    overflow: hidden;
    background: var(--page);
  }
  .canvas { position: relative; width: 1035px; height: 1200px; }

  /* Card back */
  .card-back {
    position: absolute;
    left: 4px; top: 0;
    width: 1031px; height: 590px;
    background: var(--charcoal);
  }
  .card-back .stripe {
    position: absolute; left: 0; width: 100%;
    background: var(--cyan);
  }
  .card-back .stripe--top { top: 156px; height: 32px; }
  .card-back .stripe--bottom { top: 398px; height: 32px; }
  .card-back .band {
    position: absolute; left: 0; top: 188px;
    width: 100%; height: 210px;
    background: var(--black);
  }

  .brand-lockup {
    position: absolute;
    display: flex; flex-direction: column; align-items: center;
    text-align: center;
  }
  .brand-mark {
    width: 58px; height: 58px;
    border-radius: 50%;
    background: var(--brand);
    margin-bottom: 18px;
  }
  .brand-name {
    font-family: "Cinzel", serif;
    font-weight: 500;
    color: var(--brand);
    letter-spacing: 2px;
    line-height: 1;
  }
  .brand-tagline {
    font-family: "Cinzel", serif;
    font-weight: 500;
    color: var(--white);
    text-transform: uppercase;
    line-height: 1;
    margin-top: 6px;
  }
  .card-back .brand-lockup { left: 0; width: 100%; top: 212px; }
  .card-back .brand-name { font-size: 34px; }
  .card-back .brand-tagline { font-size: 10px; letter-spacing: 0.6px; }

  /* Card front */
  .card-front {
    position: absolute;
    left: 4px; top: 612px;
    width: 1031px; height: 588px;
  }
  .card-front .identity-panel {
    position: absolute; left: 0; top: 0;
    width: 472px; height: 514px;
    background: var(--charcoal);
  }
  .card-front .contact-panel {
    position: absolute; left: 472px; top: 0;
    width: 559px; height: 514px;
    background: var(--cyan);
  }
  .card-front .base-strip {
    position: absolute; left: 0; top: 514px;
    width: 100%; height: 74px;
    background: var(--black);
  }
  .card-front .brand-lockup { left: 0; width: 472px; top: 182px; }
  .card-front .brand-name { font-size: 38px; }
  .card-front .brand-tagline { font-size: 11px; letter-spacing: 0.6px; }

  .person {
    position: absolute; left: 0; top: 52px;
    width: 100%;
    text-align: center;
    font-family: "Source Sans 3", sans-serif;
    color: var(--ink);
  }
  .person-name { font-size: 56px; line-height: 1.1; font-weight: 400; }
  .person-role { font-size: 32px; line-height: 1.2; margin-top: 4px; }

  .contact-list {
    position: absolute; left: 94px; top: 262px;
    list-style: none;
    font-family: "Source Sans 3", sans-serif;
    color: var(--ink);
  }
  .contact-item {
    display: flex; align-items: flex-start;
    margin-bottom: 26px;
  }
  .contact-icon { width: 40px; height: 40px; flex: none; margin-right: 12px; }
  .contact-address { font-size: 23px; line-height: 32px; margin-top: -2px; }
  .contact-phone { font-size: 30px; line-height: 40px; }
  .contact-email { font-size: 24px; line-height: 40px; }
</style>
</head>
<body>
<main class="canvas">

  <section class="card-back" aria-label="Business card back">
    <div class="stripe stripe--top"></div>
    <div class="band"></div>
    <div class="stripe stripe--bottom"></div>
    <div class="brand-lockup">
      <span class="brand-mark"></span>
      <span class="brand-name">ARDENWELL</span>
      <span class="brand-tagline">Building and Property Services</span>
    </div>
  </section>

  <section class="card-front" aria-label="Business card front">
    <div class="identity-panel">
      <div class="brand-lockup">
        <span class="brand-mark"></span>
        <span class="brand-name">ARDENWELL</span>
        <span class="brand-tagline">Building and Property Services</span>
      </div>
    </div>

    <div class="contact-panel">
      <div class="person">
        <h1 class="person-name">Duncan Ferris</h1>
        <p class="person-role">Director</p>
      </div>

      <ul class="contact-list">
        <li class="contact-item">
          <svg class="contact-icon" viewBox="0 0 40 40" aria-hidden="true">
            <rect x="1" y="1" width="38" height="38" rx="7" fill="#fff"/>
            <path d="M20 6c-6 0-10.5 4.5-10.5 10.2C9.5 24 20 34 20 34s10.5-10 10.5-17.8C30.5 10.5 26 6 20 6z" fill="#0b0b0b"/>
            <circle cx="20" cy="16.5" r="4.2" fill="#fff"/>
          </svg>
          <span class="contact-address">Level 17, 82 Harlow Street, MERRIDALE,<br>Melbourne, Vic 3094</span>
        </li>
        <li class="contact-item">
          <svg class="contact-icon" viewBox="0 0 40 40" aria-hidden="true">
            <rect x="1" y="1" width="38" height="38" rx="7" fill="#fff"/>
            <path d="M11 9.5l5-1.5 3 7-3.2 2.3c1.4 3 3.8 5.4 6.9 6.9l2.3-3.2 7 3-1.5 5c-.4 1.2-1.6 2-2.9 1.9C17.5 30 10 22.5 9.1 12.4c-.1-1.3.7-2.5 1.9-2.9z" fill="#0b0b0b"/>
          </svg>
          <span class="contact-phone">9518 2736</span>
        </li>
        <li class="contact-item">
          <svg class="contact-icon" viewBox="0 0 40 40" aria-hidden="true">
            <rect x="1" y="1" width="38" height="38" rx="7" fill="#fff"/>
            <rect x="6" y="9" width="28" height="22" rx="3" fill="#0b0b0b"/>
            <path d="M9 12l22 16M31 12L9 28" stroke="#fff" stroke-width="3" stroke-linecap="round"/>
          </svg>
          <span class="contact-email">dunardenwell@mailbox-example.com</span>
        </li>
      </ul>
    </div>

    <div class="base-strip"></div>
  </section>

</main>
</body>
</html>
```